TBV business card

For a business card with our logo

Contact Information for Business Card

Lucien MARVET
Founder & CEO
email : ceo@brightlanternstudio.com / www.brightlanternstudio.com /
instagram / facebook / WhatsApp
N°: +590 690 482 517

Colors

Designer to choose colors to be used in the design.

```html
<!DOCTYPE html>
<html lang="en">
<head>
<meta charset="utf-8">
<title>TBV business card</title>
<link rel="stylesheet" href="https://fonts.googleapis.com/css2?family=Catamaran:wght@400;600;700&display=swap">
<style>
  :root {
    --page: #e2e2e2;
    --card: #000000;
    --orange: #f07325;
    --blue: #1f5aa6;
    --white: #ffffff;
  }
  * { margin: 0; padding: 0; box-sizing: border-box; }
  html, body {
    width: 1200px; height: 960px; overflow: hidden;
    background: var(--page);
    font-family: "Catamaran", "Helvetica Neue", Arial, sans-serif;
  }
  .canvas { position: relative; width: 1200px; height: 960px; }
  .card {
    position: absolute; left: 267px; width: 671px;
    background: var(--card); overflow: hidden;
  }
  .card--back { top: 77px; height: 385px; }
  .card--front { top: 492px; height: 382px; }
  .edge { position: absolute; top: 0; bottom: 0; width: 17px; background: var(--orange); }
  .edge--left { left: 0; }
  .edge--right { right: 0; }

  .brand { position: absolute; text-align: center; }
  .brand__dot {
    display: block; margin: 0 auto;
    width: 64px; height: 64px; border-radius: 50%; background: var(--orange);
  }
  .brand__name {
    display: block; margin-top: 8px;
    color: var(--blue); font-weight: 600; font-size: 19px;
    letter-spacing: 0.5px; white-space: nowrap; line-height: 1;
  }
  .card--back .brand { left: 0; right: 0; top: 145px; }
  .card--front .brand { left: 40px; width: 200px; top: 55px; }

  .web-line {
    position: absolute; left: 0; right: 0; top: 338px;
    text-align: center; color: var(--orange);
    font-weight: 600; font-size: 17px;
  }

  .social { position: absolute; top: 30px; right: 47px; display: flex; gap: 11px; }
  .social__item { width: 24px; height: 24px; border-radius: 50%; background: var(--white); }

  .person { position: absolute; right: 48px; top: 188px; text-align: right; color: var(--white); }
  .person__name { font-size: 27px; line-height: 1.1; font-weight: 400; }
  .person__first { color: var(--orange); font-weight: 700; }
  .person__role { font-size: 18px; line-height: 1.2; }

  .contacts { position: absolute; left: 50px; top: 220px; list-style: none; }
  .contacts__row {
    display: flex; align-items: center; height: 28px;
    color: var(--white); font-size: 17.5px;
  }
  .contacts__icon { width: 20px; height: 20px; margin-right: 12px; flex: none; }
  .contacts__row + .contacts__row { margin-top: 0; }
</style>
</head>
<body>
<main class="canvas">

  <section class="card card--back">
    <div class="edge edge--left"></div>
    <div class="edge edge--right"></div>
    <div class="brand">
      <span class="brand__dot"></span>
      <span class="brand__name">BRIGHT LANTERN STUDIO</span>
    </div>
    <p class="web-line">www.brightlanternstudio.com</p>
  </section>

  <section class="card card--front">
    <div class="edge edge--right"></div>
    <div class="brand">
      <span class="brand__dot"></span>
      <span class="brand__name">BRIGHT LANTERN STUDIO</span>
    </div>

    <div class="social" aria-label="Social profiles">
      <span class="social__item"></span>
      <span class="social__item"></span>
      <span class="social__item"></span>
    </div>

    <div class="person">
      <p class="person__name"><span class="person__first">LUCIEN</span> MARVET</p>
      <p class="person__role">Founder &amp; CEO</p>
    </div>

    <ul class="contacts">
      <li class="contacts__row">
        <svg class="contacts__icon" viewBox="0 0 24 24" aria-hidden="true">
          <path fill="#f07325" d="M6.6 10.8a15 15 0 0 0 6.6 6.6l2.2-2.2c.3-.3.7-.4 1-.2 1.1.4 2.3.6 3.6.6.6 0 1 .4 1 1V20c0 .6-.4 1-1 1A17 17 0 0 1 3 4c0-.6.4-1 1-1h3.5c.6 0 1 .4 1 1 0 1.3.2 2.5.6 3.6.1.3 0 .7-.2 1z"/>
        </svg>
        +590 690 482 517
      </li>
      <li class="contacts__row">
        <svg class="contacts__icon" viewBox="0 0 24 24" aria-hidden="true">
          <rect x="1" y="5" width="22" height="14" fill="#f07325"/>
          <path d="M1 5l11 8 11-8M1 19l8-7M23 19l-8-7" fill="none" stroke="#000" stroke-width="1.4"/>
        </svg>
        ceo@brightlanternstudio.com
      </li>
      <li class="contacts__row">
        <svg class="contacts__icon" viewBox="0 0 24 24" aria-hidden="true">
          <path fill="#f07325" d="M6 2l13 12h-6.5l3.5 7.5-2.6 1.2-3.5-7.6L6 19.5z"/>
        </svg>
        www.brightlanternstudio.com
      </li>
    </ul>
  </section>

</main>
</body>
</html>
```